Refresh Logo and Website for new Greek Food Business

Please see newest direction of the logo with image below and "food items, cross, olive branch, warrior, philosopher face, spear" sticking out of the top of roof? Perhaps blue door with the font there "The Aegean Hut" (See IMG 5685 and IMG5686 below).

Looking for a REFESHED LOGO that features "The Aegean Hut" with the HUT more obvious AND more of a play on food while still including the two characters:
philosopher and warrior! Our tag line is "Hope, Home, Harmony, and Happy Plates!"

Once logo is solidified looking to have the website built out in a form that I can update myself (preferably WORD PRESS).

The Aegean Hut is a mobile food business in Pennsylvania, USA that specializes in Greek salad bowls and Greek sandwiches.

I have hosting through Hostcrane.com and the domain name will be www.theaegeanhut.com. We will use a POS system like TALLYPAD for our on site and online ordering. I am not very familiar with how their technology integrates into our site, but from similar restaurants such as "pita pals" it appears that it is a different page.

Need something artistic like this:
https://www.artfolio.example/gallery/48210953/Koralo-Greek-Restaurant

The Graphic work above with KORALO Greek Restaurant is AMAZING! Instead of dancing characters we insert the warrior and philosopher characters .. These characters will be on our packaging and branding and shirts and menu.

https://www.burrowbite.example/ - All the Functionality of...
https://globalmarkstudio.example/branding-packaging-design-for-olive-ember-kitchen-restaurant-in-the-netherlands/ - Love the cartoon, happy, professional, classy look
https://auntmiras.example/ - Like the Blue Truck Imagery for Catering
https://www.pitapals.example/ - Love the big photos, look, and feel

The site map would include:
HomePage which would include all the sections below BUT on the same page scrolling down (I don't want different pages).
Online Ordering (Link)
Menu
About Us
Team
Catering
Contact Us
Location and Hours
Careers
Bottom includes social media links

I prefer a site that just scrolls down to the bottom. I have created a "bookmark/placeholder page" already for the www.theaegeanhut.com, but I don't like it. It is just a placeholder for now. We need something bright, engaging, happy, and deliciously cartoonish!

I need something I can edit (wordpress) easily too.

Thank you everyone for your hard work. We are down to the last four days of this design competition. PLEASE ensure that you include artwork that shows Hope, Home, Harmony and Happy Plates throughout the theme of the website. Use the Greco Roman warriors, Athenian philosophers, Greek Santorini Churches, Greek Food throughout website.

Target Market(s)

Families of USA

Industry/Entity Type

Food Service

Coding

Coded - Design and coding required

Number of Pages Required

1 page

Font styles to use
Other font styles liked:
• Some form of legible GREEK LOOKING FONT LETTERS

Colors

Designer to choose colors to be used in the design.

Requirements
Must have
• Book Us Page, Order Now Page, Careers Page, Big Photos of Trailer and Team and Food BUT need the Logo theme of cartoon like things clear and obvious!!!
Nice to have
• Logo should include "HUT/Parthenon like structure made of wood, stone, food even?
Should not have
• I don't want "realistic photos" of food.

```html
<!DOCTYPE html>
<html lang="en">
<head>
<meta charset="utf-8">
<title>The Aegean Hut</title>
<link rel="stylesheet" href="https://fonts.googleapis.com/css2?family=Playfair+Display:wght@700;800&family=Vollkorn:wght@400;600;700&family=Roboto:wght@400;500&display=swap">
<style>
:root{
  --blue:#1767b5;
  --blue-dark:#0f5aa3;
  --ink:#1f1f1f;
  --text:#333;
  --light:#f3f3f3;
  --pale-blue:#e9eff7;
  --footer:#1d1d1d;
  --white:#fff;
  --head:"Playfair Display",Georgia,serif;
  --body:"Vollkorn",Georgia,serif;
  --sans:"Roboto",Arial,sans-serif;
}
*{box-sizing:border-box;margin:0;padding:0}
html,body{width:1200px;height:4137px;overflow:hidden}
body{position:relative;background:var(--white);font-family:var(--body);color:var(--text)}
.section{position:absolute;left:0;width:1200px}
.btn{position:absolute;display:flex;align-items:center;justify-content:space-between;background:var(--blue);color:var(--white);border-radius:24px;font-family:var(--body);font-weight:700;font-size:14px;letter-spacing:.5px;padding:0 10px 0 22px;text-transform:uppercase}
.btn .dot{width:18px;height:18px;border-radius:50%;background:#111;display:flex;align-items:center;justify-content:center}
.btn.light{background:var(--white);color:var(--blue)}
.btn.light .dot{background:var(--blue)}
.section-title{position:absolute;left:0;width:1200px;text-align:center;font-family:var(--head);font-weight:700;font-size:32px;color:var(--ink)}
.section-title::after{content:"";display:block;width:40px;height:3px;background:var(--blue);margin:10px auto 0}

/* nav */
.site-nav{top:0;height:77px;background:var(--white);border-top:3px solid var(--blue);z-index:5}
.brand{position:absolute;left:116px;top:14px;display:flex;align-items:center;gap:10px}
.brand .mark{width:48px;height:48px;border-radius:50%;background:var(--blue)}
.brand .name{font-family:var(--body);font-weight:700;font-size:18px;color:var(--blue)}
.nav-links{position:absolute;left:398px;top:30px;display:flex;gap:40px;font-family:var(--body);font-size:13px;letter-spacing:1px;color:#333}
.nav-links .active{color:var(--blue)}
.nav-cta{left:938px;top:19px;width:150px;height:42px;font-size:13px}

/* hero */
.hero{top:77px;height:710px}
.hero-photo{position:absolute;inset:0;background:linear-gradient(180deg,#4f8aa6 0%,#7fb3c0 28%,#a9c6b8 42%,#c9c6a6 55%,#9b8c6c 75%,#5a4e3e 100%)}
.hero-panel{position:absolute;left:135px;top:210px;width:952px;height:200px;background:rgba(40,50,60,.45)}
.hero-title{position:absolute;left:135px;top:235px;width:952px;text-align:center;font-family:var(--head);font-weight:700;font-size:46px;color:var(--white)}
.hero-order{left:527px;top:317px;width:165px;height:40px;font-size:13px}
.hero-arrow{position:absolute;top:330px}
.torn{position:absolute;left:0;width:1200px}

/* about */
.about{top:787px;height:546px}
.about-art{position:absolute;left:109px;top:117px;width:464px;height:305px;border-radius:12px;background:linear-gradient(90deg,#b5432f 0%,#9a8a7a 30%,#8f8f95 50%,#e0c24a 72%,#f3df6e 100%)}
.about-title{position:absolute;left:589px;top:108px;font-family:var(--head);font-weight:700;font-size:34px;color:var(--ink)}
.about-title span{color:var(--blue)}
.about-text{position:absolute;left:589px;top:170px;width:474px;font-size:16.5px;line-height:25px;text-align:justify}
.about-btn{left:588px;top:392px;width:165px;height:45px}

/* menus */
.menus{top:1333px;height:639px;background:var(--light)}
.menus-title{top:75px}
.menu-card{position:absolute;width:212px;background:var(--white);border-radius:106px;box-shadow:0 8px 18px rgba(0,0,0,.18);text-align:center}
.menu-card.open{border:2px solid var(--blue)}
.menu-art{position:absolute;left:36px;width:140px;height:150px;border-radius:70px;background:linear-gradient(180deg,#dde5ef,#c3cfde)}
.menu-name{position:absolute;left:0;width:100%;font-family:var(--head);font-weight:700;font-size:21px;line-height:32px;color:var(--ink);letter-spacing:.5px}
.menu-desc{position:absolute;left:14px;width:184px;font-size:12px;line-height:16px;color:#444}
.menu-toggle{position:absolute;left:85px;width:42px;height:42px;border-radius:50%;background:var(--blue);color:var(--white);font-family:var(--sans);font-size:20px;line-height:42px;text-align:center}

/* team */
.team{top:1972px;height:643px;background:linear-gradient(180deg,#1466b5,#0f62b0)}
.team .section-title{top:80px;color:var(--white)}
.team .section-title::after{background:var(--white)}
.team-card{position:absolute;top:186px;width:310px;height:278px;border-radius:10px;overflow:hidden}
.team-photo{position:absolute;inset:0}
.team-shade{position:absolute;left:0;right:0;bottom:0;height:120px;background:linear-gradient(180deg,rgba(0,0,0,0),rgba(0,0,0,.78))}
.team-name{position:absolute;left:0;width:100%;top:212px;text-align:center;font-family:var(--head);font-weight:700;font-size:22px;color:var(--white);letter-spacing:1px}
.team-role{position:absolute;left:0;width:100%;top:245px;text-align:center;font-family:var(--sans);font-style:italic;font-size:14px;color:var(--white)}
.team-btn{left:530px;top:495px;width:140px;height:43px;font-size:13px}

/* contact */
.contact{top:2615px;height:594px}
.contact .section-title{top:80px}
.contact-intro{position:absolute;left:270px;top:155px;width:660px;text-align:center;font-size:16px;line-height:25px}
.map{position:absolute;left:141px;top:216px;width:383px;height:243px;border:4px solid var(--blue);border-radius:6px;background:#eceeea}
.hours{position:absolute;top:475px;font-family:var(--sans);font-size:14px;color:#333}
.hours b{display:block;font-weight:500;margin-top:3px;color:#111}
.field{position:absolute;height:41px;border:1px solid #cfcfcf;border-radius:4px;display:flex;align-items:center;gap:8px;padding-left:10px;font-family:var(--body);font-size:13px;color:#666}
.field svg{flex:none}
.field.message{align-items:flex-start;padding-top:12px}
.submit-btn{left:552px;top:462px;width:124px;height:43px;font-size:13px}

/* careers */
.careers{top:3209px;height:509px;background:var(--pale-blue)}
.careers-title{position:absolute;right:612px;top:82px;font-family:var(--head);font-weight:700;font-size:34px;color:var(--ink)}
.careers-text{position:absolute;left:112px;top:143px;width:473px;font-size:16.5px;line-height:25px;text-align:justify;text-align-last:right}
.careers-btn{left:418px;top:364px;width:165px;height:45px}
.careers-art{position:absolute;top:85px;width:212px;height:300px;border-radius:10px}

/* footer */
.footer{top:3718px;height:419px;background:var(--footer);color:var(--white)}
.footer-brand{position:absolute;left:185px;top:155px;display:flex;align-items:center;gap:10px}
.footer-brand .mark{width:40px;height:40px;border-radius:50%;background:var(--blue)}
.footer-brand .name{font-family:var(--body);font-weight:700;font-size:20px;color:var(--white)}
.footer-col{position:absolute;top:92px}
.footer-col h4{font-family:var(--head);font-weight:700;font-size:19px;letter-spacing:.5px}
.footer-col h4::after{content:"";display:block;width:50px;height:2px;background:var(--blue);margin-top:8px}
.footer-col ul{list-style:none;margin-top:18px;font-family:var(--body);font-weight:700;font-size:12.5px;line-height:26px;letter-spacing:.3px}
.footer-rule{position:absolute;left:112px;top:337px;width:976px;height:1px;background:#3a3a3a}
.copyright{position:absolute;left:0;width:1200px;top:362px;text-align:center;font-family:var(--body);font-size:14px}
.to-top{position:absolute;left:1129px;top:305px;width:40px;height:40px;border-radius:5px;background:var(--blue);display:flex;align-items:center;justify-content:center}
</style>
</head>
<body>

<header class="section site-nav">
  <div class="brand"><span class="mark"></span><span class="name">The Aegean Hut</span></div>
  <nav class="nav-links">
    <span class="active">HOME</span><span>MENU</span><span>ABOUT US</span><span>TEAM</span><span>CATERING</span><span>CAREERS</span>
  </nav>
  <div class="btn nav-cta">Contact Us <span class="dot"><svg width="8" height="8" viewBox="0 0 8 8"><path d="M2 1l3 3-3 3" stroke="#fff" stroke-width="1.5" fill="none"/></svg></span></div>
</header>

<section class="section hero">
  <div class="hero-photo" role="img" aria-label="Photo of the cream food truck with the round blue badge, parked by a palm-lined beach"></div>
  <div class="hero-panel"></div>
  <h1 class="hero-title">Hope, Home, Harmony, and Happy Plates</h1>
  <div class="btn hero-order">Order Online <span class="dot"><svg width="8" height="8" viewBox="0 0 8 8"><path d="M2 1l3 3-3 3" stroke="#fff" stroke-width="1.5" fill="none"/></svg></span></div>
  <svg class="hero-arrow" style="left:44px" width="32" height="66" viewBox="0 0 32 66"><path d="M30 2L2 33l28 31" stroke="#fff" stroke-width="2.5" fill="none"/></svg>
  <svg class="hero-arrow" style="left:1124px" width="32" height="66" viewBox="0 0 32 66"><path d="M2 2l28 31L2 64" stroke="#fff" stroke-width="2.5" fill="none"/></svg>
  <svg class="torn" style="top:670px" width="1200" height="42" viewBox="0 0 1200 42" preserveAspectRatio="none"><path d="M0 30L40 22 80 34 130 18 180 30 230 20 290 34 340 16 400 28 460 22 520 32 580 14 640 30 700 20 760 32 820 18 880 30 940 22 1000 34 1060 18 1120 30 1160 22 1200 28V42H0z" fill="#fff"/></svg>
</section>

<section class="section about">
  <div class="about-art" role="img" aria-label="Cartoon illustration of three Greco-Roman warriors in red, steel and gold armour with spears and a round shield"></div>
  <h2 class="about-title">ABOUT <span>US</span></h2>
  <p class="about-text">Saerspiciatis undeasepoiise omnis sesisadi isiste natus error sit voluptatem accusan tium doloremque laudantium, totam rem aperiam, ease aqskse soue ipaefdsa quae abillo inventore veritatis easequasi archilk jsetecto beatae vitae dicta sunt explicabo. Nemoenim ipskl seae ioam voluptatemquia volupta sde sessitasese aspernatur saeiklo sauoditsaut fugitsdsed quia consequuntur magni dolores eos qui ratione voluptatem sequi nesciunt.</p>
  <div class="btn about-btn">Learn More <span class="dot"><svg width="8" height="8" viewBox="0 0 8 8"><path d="M2 1l3 3-3 3" stroke="#fff" stroke-width="1.5" fill="none"/></svg></span></div>
</section>

<section class="section menus">
  <svg class="torn" style="top:-40px" width="1200" height="42" viewBox="0 0 1200 42" preserveAspectRatio="none"><path d="M0 14L50 24 100 10 160 26 220 12 280 28 340 14 400 24 460 8 520 26 580 14 640 28 700 12 760 24 820 10 880 26 940 14 1000 28 1060 12 1120 24 1200 16V42H0z" fill="#f3f3f3"/></svg>
  <h2 class="section-title menus-title">MENUS</h2>

  <div class="menu-card" style="left:112px;top:180px;height:369px">
    <div class="menu-art" style="top:24px" role="img" aria-label="Cartoon warrior kneeling with a fish on his spear"></div>
    <div class="menu-name" style="top:218px">CONSECTETUR<br>ADIPISCIN</div>
    <div class="menu-toggle" style="top:313px">+</div>
  </div>

  <div class="menu-card open" style="left:366px;top:144px;height:402px">
    <div class="menu-art" style="top:16px" role="img" aria-label="Cartoon warrior in a purple cape holding a lobster on his spear"></div>
    <div class="menu-name" style="top:213px">INCIDIDUNT</div>
    <p class="menu-desc" style="top:255px">Saerspiciatis undeasepoliise omnis sesisadi isiste natus error sit voluptatem accusan tium doloremque laudantium.</p>
    <div class="menu-toggle" style="top:349px">-</div>
  </div>

  <div class="menu-card" style="left:620px;top:180px;height:369px">
    <div class="menu-art" style="top:24px" role="img" aria-label="Cartoon warrior with a long sword standing beside a lamb"></div>
    <div class="menu-name" style="top:218px">EIUSMOD<br>TEMPOR</div>
    <div class="menu-toggle" style="top:313px">+</div>
  </div>

  <div class="menu-card" style="left:874px;top:180px;height:369px">
    <div class="menu-art" style="top:24px" role="img" aria-label="Cartoon warrior with a shield raising a roast leg of meat"></div>
    <div class="menu-name" style="top:218px">ACCUSANTIUM<br>DOLOREM</div>
    <div class="menu-toggle" style="top:313px">+</div>
  </div>
</section>

<section class="section team">
  <h2 class="section-title">OUR TEAM</h2>
  <div class="team-card" style="left:112px">
    <div class="team-photo" role="img" aria-label="Portrait photo of a smiling team member in a denim shirt" style="background:linear-gradient(180deg,#8fb0cf 0%,#5f86b0 55%,#3d5f86 100%)"></div>
    <div class="team-shade"></div>
    <div class="team-name">MARCO DELVANE</div><div class="team-role">CEO</div>
  </div>
  <div class="team-card" style="left:445px">
    <div class="team-photo" role="img" aria-label="Portrait photo of a smiling team member in a grey blazer" style="background:linear-gradient(180deg,#ececec 0%,#b9b9b9 55%,#5c5c5c 100%)"></div>
    <div class="team-shade"></div>
    <div class="team-name">ELENA VARKOSI</div><div class="team-role">CEO</div>
  </div>
  <div class="team-card" style="left:777px">
    <div class="team-photo" role="img" aria-label="Photo of a chef in a blue apron preparing food in a kitchen" style="background:linear-gradient(180deg,#d9d5cf 0%,#8f8c8a 50%,#3f4a5e 100%)"></div>
    <div class="team-shade"></div>
    <div class="team-name">NORA KESSLING</div><div class="team-role">CEO</div>
  </div>
  <div class="btn light team-btn">View All <span class="dot"><svg width="8" height="8" viewBox="0 0 8 8"><path d="M2 1l3 3-3 3" stroke="#fff" stroke-width="1.5" fill="none"/></svg></span></div>
</section>

<section class="section contact">
  <h2 class="section-title">CONTACT US</h2>
  <p class="contact-intro">Saerspiciatis undeasepoiise omnis sesisadi isiste natus error sit voluptatem accusan tium doloremque laudantium totam rem aperiam.</p>
  <div class="map" role="img" aria-label="Street map marking the truck location"></div>
  <div class="hours" style="left:165px">Mon - Fri<b>10:00 - 08:00</b></div>
  <div class="hours" style="left:345px">Sat - Sun<b>11:00 - 09:00</b></div>

  <div class="field" style="left:552px;top:216px;width:261px"><svg width="10" height="11" viewBox="0 0 10 11"><circle cx="5" cy="3" r="2.5" fill="#1767b5"/><path d="M0 11c0-4 10-4 10 0z" fill="#1767b5"/></svg>First Name</div>
  <div class="field" style="left:823px;top:216px;width:261px"><svg width="10" height="11" viewBox="0 0 10 11"><circle cx="5" cy="3" r="2.5" fill="#1767b5"/><path d="M0 11c0-4 10-4 10 0z" fill="#1767b5"/></svg>Last Name</div>
  <div class="field" style="left:552px;top:269px;width:261px"><svg width="11" height="8" viewBox="0 0 11 8"><rect width="11" height="8" fill="#1767b5"/><path d="M0 0l5.5 4.5L11 0" stroke="#fff" fill="none"/></svg>Email</div>
  <div class="field" style="left:823px;top:269px;width:261px"><svg width="10" height="10" viewBox="0 0 10 10"><path d="M2 0l2 2.5-1.2 1.4c.8 1.5 1.8 2.5 3.3 3.3L7.5 6 10 8 8.5 10C4 10 0 6 0 1.5z" fill="#1767b5"/></svg>Phone</div>
  <div class="field message" style="left:552px;top:322px;width:532px;height:122px"><svg width="10" height="10" viewBox="0 0 10 10"><path d="M1 9l1-3 6-6 2 2-6 6z" fill="#1767b5"/></svg>Enter Your Message</div>
  <div class="btn submit-btn">Submit <span class="dot"><svg width="8" height="8" viewBox="0 0 8 8"><path d="M2 1l3 3-3 3" stroke="#fff" stroke-width="1.5" fill="none"/></svg></span></div>
</section>

<section class="section careers">
  <h2 class="careers-title">CAREERS</h2>
  <p class="careers-text">Saerspiciatis undeasepoiise omnis sesisadi isiste natus error sit voluptatem accusan tium doloremque laudantium, totam rem aperiam, ease aqskse soue ipaefdsa quae abillo inventore veritatis easequasi archilk jsetecto beatae vitae dicta sunt explicabo. Nemoenim ipskl seae ioam voluptatemquia volupta sde sessitasese aspernatur saeiklo sauoditsaut fugitsdsed quia consequuntur magni dolores eos qui ratione voluptatem sequi nesciunt.</p>
  <div class="btn careers-btn">Learn More <span class="dot"><svg width="8" height="8" viewBox="0 0 8 8"><path d="M2 1l3 3-3 3" stroke="#fff" stroke-width="1.5" fill="none"/></svg></span></div>
  <div class="careers-art" style="left:641px;background:linear-gradient(180deg,#b08560 0%,#8a5a3c 55%,#5e3a28 100%)" role="img" aria-label="Cartoon warrior in a horned helmet and fur-trimmed armour"></div>
  <div class="careers-art" style="left:853px;background:linear-gradient(180deg,#5a5f6a 0%,#3a3e47 55%,#24272e 100%)" role="img" aria-label="Cartoon knight in dark armour with a plumed helmet"></div>
</section>

<footer class="section footer">
  <svg class="torn" style="top:-30px" width="1200" height="32" viewBox="0 0 1200 32" preserveAspectRatio="none"><path d="M0 12L60 20 110 6 170 18 230 8 300 22 360 10 420 20 480 4 540 18 600 10 660 22 720 6 780 18 840 10 900 20 960 6 1020 18 1080 10 1140 20 1200 12V32H0z" fill="#1d1d1d"/></svg>
  <div class="footer-brand"><span class="mark"></span><span class="name">The Aegean Hut</span></div>
  <div class="footer-col" style="left:438px"><h4>QUICK LINKS</h4><ul><li>HOME</li><li>MENU</li><li>ABOUT US</li><li>TEAM</li><li>CATERING</li><li>CONTACT US</li></ul></div>
  <div class="footer-col" style="left:665px"><h4>LINKS</h4><ul><li>COPYRIGHT</li><li>LEGAL</li><li>PRIVACY</li><li>ACCESSIBILITY</li><li>SITEMAP</li></ul></div>
  <div class="footer-col" style="left:843px"><h4>SUPPORT</h4><ul><li>TEAM</li><li>CAREERS</li><li>OUR VALUES</li><li>LOCATION AND HOURS</li><li>CAREERS</li></ul></div>
  <div class="to-top"><svg width="12" height="8" viewBox="0 0 12 8"><path d="M1 7l5-5 5 5" stroke="#fff" stroke-width="1.6" fill="none"/></svg></div>
  <div class="footer-rule"></div>
  <p class="copyright">©2023. All rights reserved.</p>
</footer>

</body>
</html>
```